Modern Dry eye Poster for eye center, Optometrist office

We need a banner to connect to patient about dry eye and treatment. Ask if patient has dry eyes and we offer treatment .
What is dry eye?
Are you suffering for dry, gritty, painful eyes, blurred vision, redness..

Now there is a quick, comfortable and affordable procedure offering relief tofdry eye.

Schedule your dry eye treatment today.

Target Market(s)

Dry eye patient

Font styles to use
Sans Serif

Colors
00a990
ffffff
0492cd
fbf289
85cae6

Requirements
Must have
• Modern design, dry eye patient
Nice to have
• real life model of nice eyes
Should not have
• No cartoon,

```html
<!DOCTYPE html>
<html lang="en">
<head>
<meta charset="UTF-8">
<title>What is Dry Eye? — Clearview Optometry</title>
<link rel="stylesheet" href="https://fonts.googleapis.com/css2?family=Montserrat:ital,wght@0,400;0,600;0,700;0,800;1,400;1,700&display=swap">
<style>
  :root {
    --yellow: #f7c531;
    --yellow-soft: #fbf289;
    --yellow-deep: #f2b705;
    --ink: #1d1d1b;
    --ink-soft: #333333;
    --white: #ffffff;
    --skin-light: #e9c9b4;
    --skin-mid: #c99a82;
    --skin-dark: #8a5d4a;
  }
  * { margin: 0; padding: 0; box-sizing: border-box; }
  html, body { width: 849px; height: 1200px; overflow: hidden; background: var(--white); }
  .poster {
    position: relative;
    width: 849px;
    height: 1200px;
    overflow: hidden;
    background: var(--white);
    font-family: "Montserrat", Arial, sans-serif;
    color: var(--ink);
  }
  .hero-photo {
    position: absolute;
    left: 0; top: 0;
    width: 849px; height: 700px;
    background:
      radial-gradient(ellipse 200px 120px at 600px 270px, #f3ddd0 0%, rgba(243,221,208,0) 100%),
      radial-gradient(ellipse 360px 300px at 520px 330px, var(--skin-light) 0%, var(--skin-mid) 70%, var(--skin-dark) 100%);
  }
  .waves { position: absolute; left: 0; top: 0; width: 849px; height: 1200px; }
  .brand {
    position: absolute;
    left: 40px; top: 22px;
    display: flex; flex-direction: column; align-items: center;
    width: 150px;
  }
  .brand-mark {
    width: 74px; height: 74px;
    background: var(--yellow);
  }
  .brand-name {
    margin-top: 10px;
    font-size: 17px;
    font-weight: 600;
    letter-spacing: 1.5px;
    color: var(--ink-soft);
    text-align: center;
    line-height: 1.25;
    text-transform: uppercase;
  }
  .headline {
    position: absolute;
    right: 30px; top: 660px;
    text-align: right;
  }
  .headline-lead {
    font-size: 56px; font-weight: 800; color: var(--ink);
    line-height: 1;
  }
  .headline-main {
    font-size: 100px; font-weight: 800; color: var(--yellow);
    line-height: 1; margin-top: 4px; letter-spacing: 1px;
  }
  .symptoms {
    position: absolute;
    left: 32px; top: 810px;
    width: 620px;
  }
  .symptoms-title {
    font-size: 40px; font-weight: 700; color: var(--ink);
    line-height: 1.1;
  }
  .symptom-list {
    list-style: none;
    margin-top: 14px;
    margin-left: 22px;
  }
  .symptom-list li {
    position: relative;
    font-size: 27px;
    line-height: 38px;
    padding-left: 28px;
    color: var(--ink);
  }
  .symptom-list li::before {
    content: "";
    position: absolute;
    left: 0; top: 15px;
    width: 9px; height: 9px;
    border-radius: 50%;
    background: var(--ink);
  }
  .offer {
    position: absolute;
    left: 32px; top: 1092px;
    width: 790px;
    font-size: 17.5px;
    font-style: italic;
    line-height: 24px;
    color: var(--ink-soft);
  }
  .call-to-action {
    position: absolute;
    left: 32px; top: 1170px;
    font-size: 18px;
    font-weight: 700;
    font-style: italic;
    color: var(--ink-soft);
    letter-spacing: 0.3px;
  }
</style>
</head>
<body>
<main class="poster">
  <div class="hero-photo" role="img" aria-label="Close-up photo of a woman gently pulling down her lower eyelid to show a red, irritated dry eye"></div>

  <svg class="waves" viewBox="0 0 849 1200" aria-hidden="true">
    <path d="M0 0 H300 C250 60 230 160 150 230 C90 280 40 300 0 310 Z" fill="var(--white)"/>
    <path d="M560 0 H849 V110 C760 60 660 30 560 0 Z" fill="var(--yellow-soft)" opacity="0.55"/>
    <path d="M640 0 H849 V60 C780 30 710 10 640 0 Z" fill="var(--white)" opacity="0.6"/>
    <path d="M0 560 C200 640 420 660 600 620 C700 598 780 560 849 520 V1200 H0 Z" fill="var(--yellow)"/>
    <path d="M0 545 C220 620 430 640 610 600 C710 578 790 548 849 510 V540 C780 580 700 612 600 632 C420 672 200 652 0 580 Z" fill="var(--yellow-soft)"/>
    <path d="M0 600 C220 690 450 720 640 680 C730 660 800 630 849 600 V1200 H0 Z" fill="var(--white)"/>
  </svg>

  <div class="brand">
    <div class="brand-mark"></div>
    <div class="brand-name">Clearview<br>Optometry</div>
  </div>

  <header class="headline">
    <div class="headline-lead">What is</div>
    <h1 class="headline-main">DRY EYE?</h1>
  </header>

  <section class="symptoms">
    <h2 class="symptoms-title">Do you suffer with:</h2>
    <ul class="symptom-list">
      <li>Dry, Gritty, Sandy Sensation</li>
      <li>Irritated Red Eyes</li>
      <li>Burning or Stinging</li>
      <li>Blurred Vision</li>
      <li>Tender Eyelids or</li>
      <li>Watery Eyes</li>
    </ul>
  </section>

  <p class="offer">Now there is a quick, comfortable and affordable procedure offering relief tofdry eye. Dry Eye Specialist Vista Eyecare are offering a Dry Eye consultation. Assessments and treatment plan offered to help you manage your Dry Eye symptom.</p>

  <p class="call-to-action">SCHEDULE YOUR DRY EYE TREATMENT TODAY.</p>
</main>
</body>
</html>
```